Quiet Willow Business Cards
Quiet Willow Body and Beauty Therapies
Bright & Fun-filled
Noreen Baptiste
Owner/Operator OPV, DRAM, NOPREX, VERTUMA
Bermuda
brightvanspa@examplemail.net
quietwillowvisits.com
Please design a business card with rounded corners Only the logo goes on the front. Name and additional info goes on the back Coloured background please
Noreen Baptiste (in bold print) Owner/Operator OPV, DRAM, NOPREX, VERTUMA mobile: 441-555-0148 email: brightvanspa@examplemail.net web site: quietwillowvisits.com Spa therapies in the comfort of home

```html
<!DOCTYPE html>
<html lang="en">
<head>
<meta charset="utf-8">
<title>Quiet Willow Business Cards</title>
<link href="https://fonts.googleapis.com/css2?family=Open+Sans:wght@400;600;700&display=swap" rel="stylesheet">
<style>
  :root {
    --stage: #e6e7e8;
    --card-white: #ffffff;
    --green-deep: #4e8619;
    --green-mid: #78ad35;
    --green-light: #a9cf6b;
    --green-text: #5a9a1f;
    --ink-white: #ffffff;
    --shadow: rgba(0, 0, 0, 0.28);
  }
  * { margin: 0; padding: 0; box-sizing: border-box; }
  html, body { width: 1200px; height: 761px; overflow: hidden; }
  body {
    background: var(--stage);
    font-family: "Open Sans", Arial, sans-serif;
    position: relative;
  }
  .card {
    position: absolute;
    border-radius: 18px;
    overflow: hidden;
    box-shadow: 2px 4px 8px var(--shadow);
  }
  .card-back { left: 329px; top: 36px; width: 511px; height: 300px; background: var(--card-white); }
  .card-front-green {
    left: 58px; top: 391px; width: 525px; height: 305px;
    background: radial-gradient(ellipse at 50% 50%, var(--green-light) 0%, var(--green-mid) 50%, var(--green-deep) 100%);
  }
  .card-front-white { left: 638px; top: 391px; width: 531px; height: 305px; background: var(--card-white); }

  .back-shape { position: absolute; inset: 0; }

  .wordmark {
    display: flex; align-items: center; gap: 10px;
    font-weight: 600; color: var(--green-text);
  }
  .wordmark .mark-dot {
    width: 18px; height: 18px; border-radius: 50%; background: var(--green-text); flex: none;
  }
  .card-front-green .wordmark { color: var(--ink-white); }
  .card-front-green .wordmark .mark-dot { background: var(--ink-white); }

  .card-back .wordmark { position: absolute; left: 32px; top: 48px; font-size: 34px; }
  .card-front .wordmark {
    position: absolute; left: 50%; top: 50%; transform: translate(-50%, -50%);
    font-size: 44px; white-space: nowrap;
  }

  .tagline {
    position: absolute; left: 40px; top: 172px;
    color: var(--green-text); font-size: 19px; line-height: 1.3;
  }

  .owner { position: absolute; right: 34px; top: 46px; text-align: right; color: var(--ink-white); }
  .owner-name { font-weight: 700; font-size: 19px; letter-spacing: 0.3px; }
  .owner-role { font-size: 12.5px; line-height: 1.35; margin-top: 4px; }

  .contacts {
    position: absolute; left: 300px; top: 210px; list-style: none;
    color: var(--ink-white); font-size: 12px;
  }
  .contacts li { display: flex; align-items: center; gap: 6px; margin-bottom: 6px; }
  .contacts li:first-child { justify-content: flex-end; }
  .contacts svg { width: 13px; height: 13px; flex: none; }
</style>
</head>
<body>

  <section class="card card-back">
    <svg class="back-shape" viewBox="0 0 511 300" preserveAspectRatio="none" aria-hidden="true">
      <defs>
        <linearGradient id="backGreen" x1="0" y1="0" x2="1" y2="1">
          <stop offset="0" stop-color="#8dc04a"/>
          <stop offset="1" stop-color="#4e8619"/>
        </linearGradient>
      </defs>
      <path d="M262 0 C248 120 210 230 120 300 L511 300 L511 0 Z" fill="#b5d88a"/>
      <path d="M292 0 C270 120 240 235 160 300 L511 300 L511 0 Z" fill="url(#backGreen)"/>
    </svg>

    <div class="wordmark"><span class="mark-dot"></span>Quiet Willow</div>

    <p class="tagline">Spa Therapies<br>in the Comfort<br>of Home</p>

    <div class="owner">
      <p class="owner-name">Noreen Baptiste</p>
      <p class="owner-role">Owner/Operator OPV,<br>DRAM, NOPREX, VERTUMA</p>
    </div>

    <ul class="contacts">
      <li>
        <svg viewBox="0 0 16 16"><rect x="4" y="1" width="8" height="14" rx="1.5" fill="#fff"/><rect x="5.5" y="3" width="5" height="8" fill="#5a9a1f"/></svg>
        441-555-0148
      </li>
      <li>
        <svg viewBox="0 0 16 16"><circle cx="8" cy="8" r="7" fill="#fff"/><rect x="4" y="5" width="8" height="6" fill="#5a9a1f"/><path d="M4 5 L8 8.5 L12 5" stroke="#fff" stroke-width="1" fill="none"/></svg>
        brightvanspa@examplemail.net
      </li>
      <li>
        <svg viewBox="0 0 16 16"><circle cx="8" cy="8" r="7" fill="#fff"/><circle cx="8" cy="8" r="4.5" fill="none" stroke="#5a9a1f" stroke-width="1"/><path d="M3.5 8 H12.5 M8 3.5 V12.5" stroke="#5a9a1f" stroke-width="1"/></svg>
        quietwillowvisits.com
      </li>
    </ul>
  </section>

  <section class="card card-front card-front-green">
    <div class="wordmark"><span class="mark-dot"></span>Quiet Willow</div>
  </section>

  <section class="card card-front card-front-white">
    <div class="wordmark"><span class="mark-dot"></span>Quiet Willow</div>
  </section>

</body>
</html>
```